Barrel Bay Runner mobile app; beer delivery service

We are looking for a design of our app - "Barrel Bay Runner". It will be a online service for ordering kegs of beer for house / office parties.

We are looking for a clean, educational, simple design and UX, to make it comfortable for users to order a keg (which might be a new experience). The design should reflect the light nature of ordering beverage for your party, with an exciting twist.

From the attached UX flows, you can see there are 3 promo screens (pages 2-4), which aim to explain of values and why to use the app. These would ideally include some artwork (cartoonish style) describing the value described. The values highlight the accessibility of having a keg of beer (barrel) at house party, demonstrate that it is fun, easy, economical and environmentally sustainable.

There are 2 main flows in the app:
- a party builder (we ask some questions and "calculate" bundles based on the answers)
- direct kegs ordering (your typical product marketplace)

Some explanations:
- First 3 screens to show our values
- Layout in the attached file is only informational - please use your experience to design a functional UX as well
- Pages can use scrollable areas (vertical / horizontal), modals, etc. We will use FlintKit so you can use those components in your design.
- Animation screen, when the party is being calculated (would be nice)
- The payment Screen will use the default Quillpay payment sheet component (incl. Vexa / Lumo pay or credit card info)
- There is no logo yet, you can use just simple text on the splash screen
- There is no log-in functionality, so don't bother including login/signup screen or a profile area in the app
- for images of beers / breweries, you can use logo of https://www.tallowmerebrewing.co.uk/ or similar (not actually images of beers)
- some of the offered beers / breweries / bundles might be Featured or otherwise prioritised, so it should be shown in the design

Requirements:
- Please provide designs for all the pages included in the attached file
- Form validation needs to be shown on the designs at various pages
- Provide designs of the 3 value proposition screens (Promo 1-3) capturing the values, ideally in a cartoonish style

Target Market(s)

Households

Industry/Entity Type

Food and beverage, delivery

Font styles to use
Sans Serif

Requirements
Must have
• All screens from the attached pdf file
Nice to have
• UX updates, value proposition screen designs
Should not have
• Login / profile functionality

```html
<!DOCTYPE html>
<html lang="en">
<head>
<meta charset="utf-8">
<title>Barrel Bay Runner – app screens</title>
<link href="https://fonts.googleapis.com/css2?family=Roboto:wght@400;500;700&display=swap" rel="stylesheet">
<style>
:root{
  --canvas:#dbd7cc;
  --brown:#5c4a26;
  --brown-dark:#4a3b1e;
  --brown-soft:#7a6538;
  --ink:#2a2418;
  --muted:#7d7666;
  --field:#eeece8;
  --field-line:#bdb8ae;
  --white:#ffffff;
  --error:#e2463f;
}
*{box-sizing:border-box;margin:0;padding:0}
html,body{width:1200px;height:3000px;overflow:hidden}
body{background:var(--canvas);font-family:"Roboto",sans-serif;color:var(--ink);position:relative}
.phone{position:absolute;width:274px;height:591px;background:var(--white);border-radius:28px;overflow:hidden;box-shadow:0 20px 40px rgba(80,70,40,.12)}
.phone.wide{width:304px;height:638px}
.status{position:absolute;top:12px;left:14px;right:14px;display:flex;justify-content:space-between;font-size:9px;color:var(--ink)}
.status .right{display:flex;align-items:center;gap:3px}
.home-bar{position:absolute;bottom:6px;left:50%;width:68px;height:4px;margin-left:-34px;background:var(--brown);border-radius:2px}
.back{position:absolute;left:14px;top:40px}
.title{position:absolute;left:15px;font-size:19px;font-weight:500;color:var(--brown)}
.art{position:absolute;left:10px;right:10px}
.promo-panel{position:absolute;left:0;right:0;bottom:0;background:var(--brown);border-radius:26px 26px 0 0;box-shadow:0 -8px 0 var(--brown-soft)}
.promo-panel p{color:var(--white);font-size:9px;font-weight:500;line-height:17px;margin:0 26px 16px}
.arrow-btn{position:absolute;left:26px;width:38px;height:38px;border:1.5px solid var(--white);border-radius:50%;display:flex;align-items:center;justify-content:center}
.label{position:absolute;left:16px;font-size:11px;color:var(--ink)}
.field{position:absolute;left:16px;right:16px;height:48px;background:var(--field);border:1px solid var(--field-line);border-radius:7px;font-size:8.5px;color:var(--muted);padding-left:19px;display:flex;align-items:center}
.hint{position:absolute;left:16px;font-size:8px;color:var(--muted);line-height:13px}
.hint.error{color:var(--error)}
.btn{position:absolute;left:16px;right:16px;height:50px;background:var(--brown);color:var(--white);border-radius:8px;font-size:12px;font-weight:500;display:flex;align-items:center;justify-content:center}
.choice-card{position:absolute;left:14px;right:14px;background:var(--white);border-radius:10px;box-shadow:0 4px 18px rgba(0,0,0,.07)}
.choice-card p{margin:32px 22px 0;font-size:11px;line-height:18px}
.choice-card .btn{left:16px;right:16px;height:43px}
.slider-label{position:absolute;left:16px;font-size:8px;color:var(--brown)}
.slider{position:absolute;left:16px;width:212px;height:2px;background:var(--brown)}
.slider i{position:absolute;top:-4px;width:9px;height:9px;border-radius:50%;background:var(--brown)}
.slider-val{position:absolute;right:18px;font-size:14px}
.select::after{content:"";position:absolute;right:17px;top:20px;border:5px solid transparent;border-top:7px solid var(--ink)}
.featured-band{position:absolute;left:0;right:0;top:220px;bottom:0;background:var(--brown);border-radius:18px 18px 0 0}
.product{position:absolute;left:16px;right:16px;background:var(--white);border-radius:8px;box-shadow:0 4px 12px rgba(0,0,0,.08);padding:14px 14px 0}
.product .head{position:relative;height:86px;padding-right:96px}
.tag{position:absolute;top:-7px;left:10px;background:var(--brown);color:var(--white);font-size:6px;padding:2px 9px;border-radius:2px}
.brewery{font-size:8.5px;font-weight:500;white-space:nowrap}
.beer-name{font-size:15px;color:var(--brown);margin-top:3px}
.abv{font-size:7px;color:var(--muted);margin-top:3px;white-space:nowrap}
.bottles{position:absolute;border-radius:3px;background:linear-gradient(135deg,#c9c1a8,#6a6a52 45%,#3f5a6e 70%,#b89560)}
.product .bottles{right:0;top:6px;width:86px;height:76px}
.desc{font-size:6.5px;color:var(--muted);line-height:14px;margin-top:10px}
.chips{margin-top:8px;display:inline-block;background:var(--field);padding:3px 6px;font-size:7px;font-weight:700;line-height:17px}
.price-row{display:flex;justify-content:space-between;align-items:center;margin:6px 0 12px}
.price{font-size:17px;color:var(--brown);font-weight:500}
.choose{background:var(--brown);color:var(--white);font-size:9px;padding:9px 26px;border-radius:5px}
.sorry-box{position:absolute;left:16px;right:16px;top:118px;height:162px;background:var(--brown);border-radius:6px;padding:40px 10px 0}
.sorry-box p{color:var(--white);font-size:9px;line-height:16px;margin-bottom:16px}
.line-item{position:absolute;left:18px;right:18px;height:62px;border-bottom:1px solid #eee;display:flex}
.line-item .thumb{width:58px;height:52px;border-radius:3px}
.line-item .info{margin-left:12px;margin-top:4px;font-size:11.5px;color:var(--brown);font-weight:500}
.line-item .info small{display:block;font-size:7.5px;color:var(--muted);font-weight:400;margin-top:2px}
.line-item .info b{display:block;font-size:9.5px;color:var(--ink);font-weight:500;margin-top:3px}
.line-item .amt{position:absolute;right:0;top:2px;font-size:12px;color:var(--brown)}
.minus{position:absolute;right:0;top:30px;width:18px;height:18px;border-radius:50%;background:var(--brown-dark)}
.minus::after{content:"";position:absolute;left:5px;right:5px;top:8px;height:2px;background:var(--white)}
.plus{position:absolute;width:19px;height:19px;border-radius:50%;background:var(--brown-dark)}
.plus::before,.plus::after{content:"";position:absolute;background:var(--white)}
.plus::before{left:5px;right:5px;top:8.5px;height:2px}
.plus::after{top:5px;bottom:5px;left:8.5px;width:2px}
.section{position:absolute;left:18px;font-size:11.5px;font-weight:500}
.extra-card{position:absolute;height:70px;background:var(--white);border-radius:6px;box-shadow:0 3px 12px rgba(0,0,0,.08);overflow:hidden}
.extra-card h4{position:absolute;left:14px;top:28px;font-size:12px;font-weight:500;color:var(--brown)}
.extra-card small{position:absolute;left:14px;top:46px;font-size:7px;color:var(--muted);white-space:nowrap}
.extra-card .cost{position:absolute;right:14px;top:10px;font-size:12px;color:var(--brown)}
.extra-card .plus{right:16px;top:36px}
.checkout{position:absolute;left:0;right:0;bottom:0;height:110px;background:#ede9e2}
.checkout .total{position:absolute;left:18px;right:18px;top:14px;display:flex;justify-content:space-between;font-size:11.5px;font-weight:500;color:var(--brown)}
.checkout .btn{top:44px;height:52px;font-size:13px}
.extra-row{position:absolute;left:16px;right:16px;height:82px;background:var(--white);border-radius:8px;box-shadow:0 3px 14px rgba(0,0,0,.08)}
.extra-row .thumb{position:absolute;left:10px;top:14px;width:54px;height:48px;border-radius:3px}
.extra-row h4{position:absolute;left:74px;top:24px;font-size:12px;font-weight:500;color:var(--brown)}
.extra-row small{position:absolute;left:74px;top:42px;font-size:7px;color:var(--muted)}
.extra-row .cost{position:absolute;right:20px;top:16px;font-size:12px;color:var(--brown)}
.extra-row .plus{right:26px;top:40px}
</style>
</head>
<body>

<!-- Splash -->
<section class="phone" style="left:147px;top:49px;height:591px">
  <div role="img" aria-label="Blurred photo of beer kegs at a party" style="position:absolute;inset:0;background:radial-gradient(circle at 55% 45%,#6b5a38,#6f6035 40%,#7a6a3e 70%,#6d5d33)"></div>
  <svg width="274" height="110" style="position:absolute;top:0;left:0"><path d="M0 0H274V95Q137 30 0 95Z" fill="#5a4826" opacity=".55"/></svg>
  <div style="position:absolute;left:38px;top:196px;width:198px;height:198px;border-radius:50%;background:rgba(110,92,48,.85);border:2px solid rgba(95,78,40,.9);display:flex;align-items:center;justify-content:center;text-align:center;color:var(--white);font-size:24px;font-weight:500;line-height:30px">Barrel Bay<br>Runner</div>
</section>

<!-- Promo 1 -->
<section class="phone" style="left:464px;top:87px">
  <div class="status"><span>9:10</span><span class="right"><svg width="11" height="8"><path d="M0 3Q5.5-1 11 3L5.5 8Z" fill="#2a2418"/></svg>69% <svg width="5" height="8"><rect width="5" height="8" rx="1" fill="#2a2418"/></svg></span></div>
  <h1 class="title" style="top:50px">Through a bash</h1>
  <div class="art" role="img" aria-label="Cartoon delivery driver unloading beer kegs from a blue truck" style="top:100px;height:120px;background:linear-gradient(100deg,#e9eef5,#5a8fd6 40%,#2f6bc8 70%,#e9eef5)"></div>
  <div class="promo-panel" style="height:302px;padding-top:38px">
    <p>Who loves a party? We all love party, but we don't all love hav to plan for one.</p>
    <p>Are you over the anxiety that comes with being the hostess the mostess?</p>
    <p>Want to make sure your guests sufficiently fed and watered?</p>
    <p>Well when it comes to beer drinkers, we got you coverer</p>
    <div class="arrow-btn" style="top:244px"><svg width="14" height="10"><path d="M0 5H12M8 1L12 5L8 9" stroke="#fff" stroke-width="1.4" fill="none"/></svg></div>
  </div>
</section>

<!-- Promo 2 -->
<section class="phone" style="left:779px;top:126px;background:linear-gradient(#f7f8fa,#fff 50%)">
  <div class="status"><span>9:10</span><span class="right"><svg width="11" height="8"><path d="M0 3Q5.5-1 11 3L5.5 8Z" fill="#2a2418"/></svg>69% <svg width="5" height="8"><rect width="5" height="8" rx="1" fill="#2a2418"/></svg></span></div>
  <h1 class="title" style="top:64px">More Pary, Less Planning</h1>
  <div class="art" role="img" aria-label="Cartoon of friends toasting with pints of beer" style="top:115px;height:110px;background:linear-gradient(100deg,#f4f6f9,#4c8fd9 35%,#e8a93a 55%,#4fae4a 75%,#f4f6f9)"></div>
  <div class="promo-panel" style="height:302px;padding-top:38px">
    <p>No more last minute runs to the bottle shop, supermarket or local wholesalers.</p>
    <p>No more back breaking journeys carrying heavy beer bottles and cans across your neighbourhood.</p>
    <p>No more worries about fridge capacity and no more warm beers for your guests.</p>
    <div class="arrow-btn" style="top:244px"><svg width="14" height="10"><path d="M0 5H12M8 1L12 5L8 9" stroke="#fff" stroke-width="1.4" fill="none"/></svg></div>
  </div>
</section>

<!-- Promo 3 -->
<section class="phone" style="left:147px;top:793px">
  <div class="status"><span>9:10</span><span class="right"><svg width="11" height="8"><path d="M0 3Q5.5-1 11 3L5.5 8Z" fill="#2a2418"/></svg>69% <svg width="5" height="8"><rect width="5" height="8" rx="1" fill="#2a2418"/></svg></span></div>
  <h1 class="title" style="top:64px">Save money &amp; the planet</h1>
  <div class="art" role="img" aria-label="Cartoon pint glass character with banknotes flying around it" style="left:60px;right:60px;top:92px;height:170px;background:radial-gradient(ellipse at center,#f3b43a,#f8d98a 40%,#fff 72%)"></div>
  <div class="promo-panel" style="height:302px;padding-top:40px">
    <p>Finally a cost efficient, environmentally sustainable, no hassle and fun way to keep all the beer drinkers at your party smiling.</p>
    <p>Our service enables you to throw a keg party of your dreams by removing the logistical challenges so you and your guests can focus on having a good time.</p>
    <p>Never worry about your beer<br>supply again.</p>
    <div class="arrow-btn" style="top:244px"><svg width="14" height="10"><path d="M0 5H12M8 1L12 5L8 9" stroke="#fff" stroke-width="1.4" fill="none"/></svg></div>
  </div>
</section>

<!-- Before we begin -->
<section class="phone" style="left:464px;top:832px">
  <div class="status"><span>9:10</span><span class="right"><svg width="11" height="8"><path d="M0 3Q5.5-1 11 3L5.5 8Z" fill="#2a2418"/></svg>69% <svg width="5" height="8"><rect width="5" height="8" rx="1" fill="#2a2418"/></svg></span></div>
  <h1 class="title" style="top:70px">Before we begin....</h1>
  <div class="label" style="top:186px">We need to check if we deliver in your area</div>
  <div class="field" style="top:213px">Adress Lookup</div>
  <div class="hint" style="top:276px">We Only deliver selected london boroughs<br>during the pilot</div>
  <div class="label" style="top:327px">Making Sure Your are grown Up</div>
  <div class="field" style="top:354px">Adress Lookup</div>
  <div class="hint error" style="top:418px">You have to be 18 years old to use this service</div>
  <div class="btn" style="top:456px">Let the Party Begin</div>
  <div class="home-bar"></div>
</section>

<!-- Lets Start -->
<section class="phone" style="left:779px;top:871px;background:linear-gradient(#fff,#f6f6f8)">
  <div class="status"><span>9:10</span><span class="right"><svg width="11" height="8"><path d="M0 3Q5.5-1 11 3L5.5 8Z" fill="#2a2418"/></svg>69% <svg width="5" height="8"><rect width="5" height="8" rx="1" fill="#2a2418"/></svg></span></div>
  <h1 class="title" style="top:70px">Lets Start.....</h1>
  <div class="choice-card" style="top:132px;height:196px">
    <p>Are you planning a party and want to have some keg fun, but not quite sure what to order?</p>
    <div class="btn" style="top:124px">Help me plan my party</div>
  </div>
  <div class="choice-card" style="top:355px;height:198px">
    <p>Do you know exactly what you want and want to pick some delicious beer for your party?</p>
    <div class="btn" style="top:124px">Right to kegs</div>
  </div>
  <div class="home-bar"></div>
</section>

<!-- Tell us about your party -->
<section class="phone" style="left:147px;top:1537px">
  <div class="status"><span>9:10</span><span class="right"><svg width="11" height="8"><path d="M0 3Q5.5-1 11 3L5.5 8Z" fill="#2a2418"/></svg>69% <svg width="5" height="8"><rect width="5" height="8" rx="1" fill="#2a2418"/></svg></span></div>
  <h1 class="title" style="top:58px">Tell us about your Party</h1>
  <div class="label" style="top:108px">When is your party</div>
  <div class="field" style="top:135px;height:42px">Select date</div>
  <div class="hint" style="top:185px">We will pickup the empty keg the next day</div>
  <div class="label" style="top:211px">Tell us about the people attending</div>
  <div class="slider-label" style="top:238px">Booze hound (good for 8 pints)</div>
  <div class="slider" style="top:259px"><i style="left:54px"></i></div><div class="slider-val" style="top:250px">8</div>
  <div class="slider-label" style="top:276px">Thirsty but thoughtful (good for 5 pints)</div>
  <div class="slider" style="top:297px"><i style="left:54px"></i></div><div class="slider-val" style="top:288px">3</div>
  <div class="slider-label" style="top:314px">Country club bore (good for 2 pints)</div>
  <div class="slider" style="top:335px"><i style="left:54px"></i></div><div class="slider-val" style="top:326px">7</div>
  <div class="label" style="top:355px">What kind of beer do you like</div>
  <div class="field select" style="top:384px;height:42px">Beer selector</div>
  <div class="label" style="top:440px">What kind of glassware do you require?</div>
  <div class="field select" style="top:467px;height:42px">Glass selector</div>
  <div class="btn" style="top:523px">Show me Recommendation</div>
  <div class="home-bar"></div>
</section>

<!-- Here is what we think -->
<section class="phone" style="left:464px;top:1576px">
  <div class="status"><span>9:10</span><span class="right"><svg width="11" height="8"><path d="M0 3Q5.5-1 11 3L5.5 8Z" fill="#2a2418"/></svg>69% <svg width="5" height="8"><rect width="5" height="8" rx="1" fill="#2a2418"/></svg></span></div>
  <svg class="back" width="18" height="12"><path d="M17 6H2M7 1L2 6L7 11" stroke="#5c4a26" stroke-width="1.6" fill="none"/></svg>
  <h1 class="title" style="top:64px">Here is what we think..</h1>
  <div class="label" style="top:118px;right:16px;line-height:17px">Based on what you told us we think you need at least 72 pints</div>
  <div class="hint" style="top:162px;font-size:9.5px">These bundles should make your party awesome</div>
  <div class="featured-band"></div>
  <div class="product" style="top:196px">
    <span class="tag">Featured</span>
    <div class="head">
      <div class="brewery">Tallowmere Brewing</div>
      <div class="beer-name">Session IPA</div>
      <div class="abv">5.2% vol &nbsp;★ ★ ★ ★ ★</div>
      <div class="bottles" role="img" aria-label="Bottles of session IPA"></div>
    </div>
    <div class="desc">Lorem Ipsum is simply dummy text of the printing and typesetting industry. Lorem Ipsum has been the industry's standard dummy text ever since the 1500s.</div>
    <div class="chips">2x 35l keg<br>40 plastic cups<br>Simple tap</div>
    <div class="price-row"><span class="price">$110.50</span><span class="choose">Choose</span></div>
  </div>
  <div class="product" style="top:476px;height:140px">
    <div class="head">
      <div class="brewery">Tallowmere Brewing</div>
      <div class="beer-name">Session IPA</div>
      <div class="abv">5.2% vol &nbsp;★ ★ ★ ★ ★</div>
      <div class="bottles" role="img" aria-label="Bottles of session IPA"></div>
    </div>
    <div class="desc">Lorem Ipsum is simply dummy text of the printing and</div>
  </div>
</section>

<!-- So sorry -->
<section class="phone" style="left:779px;top:1615px">
  <div class="status"><span>9:10</span><span class="right"><svg width="11" height="8"><path d="M0 3Q5.5-1 11 3L5.5 8Z" fill="#2a2418"/></svg>69% <svg width="5" height="8"><rect width="5" height="8" rx="1" fill="#2a2418"/></svg></span></div>
  <svg class="back" width="18" height="12"><path d="M17 6H2M7 1L2 6L7 11" stroke="#5c4a26" stroke-width="1.6" fill="none"/></svg>
  <h1 class="title" style="top:64px">So Sorry...</h1>
  <div class="sorry-box">
    <p>Unfortunately we are not able to deliver this order to you on the requested date.</p>
    <p>Your could try different date or beer order</p>
  </div>
  <div class="home-bar"></div>
</section>

<!-- My Basket -->
<section class="phone wide" style="left:267px;top:2302px">
  <div class="status"><span>9:10</span><span class="right"><svg width="11" height="8"><path d="M0 3Q5.5-1 11 3L5.5 8Z" fill="#2a2418"/></svg>69% <svg width="5" height="8"><rect width="5" height="8" rx="1" fill="#2a2418"/></svg></span></div>
  <svg class="back" style="top:48px" width="18" height="12"><path d="M17 6H2M7 1L2 6L7 11" stroke="#5c4a26" stroke-width="1.6" fill="none"/></svg>
  <h1 class="title" style="top:78px">My Basket..</h1>
  <div class="section" style="top:116px;font-size:11px">Items</div>
  <div class="line-item" style="top:138px">
    <div class="thumb bottles" role="img" aria-label="Bottles of session IPA" style="position:static"></div>
    <div class="info">1 x Session IPA<small>Tallowmere Brewing</small><b>35l Keg</b></div>
    <span class="amt">$65</span><i class="minus"></i>
  </div>
  <div class="line-item" style="top:204px">
    <div class="thumb bottles" role="img" aria-label="Bottles of lager" style="position:static"></div>
    <div class="info">Lager<small>Tallowmere Brewing</small><b>20 Keg</b></div>
    <span class="amt">$55</span><i class="minus"></i>
  </div>
  <div class="line-item" style="top:270px;height:36px;border:none"><div class="info" style="margin:10px 0 0 18px">15 x Returnable Glasses</div><span class="amt" style="top:10px">$35</span></div>
  <div class="section" style="top:320px;font-size:11px">Recommender with your order</div>
  <div class="extra-card" style="left:14px;width:226px;top:340px"><h4>kegerator</h4><small>Keep your keg chilled throughout</small><span class="cost">+ $35.00</span><i class="plus"></i></div>
  <div class="extra-card" style="left:254px;width:80px;top:340px"><h4>kegerator</h4><small>Keep your keg</small></div>
  <div class="section" style="top:414px;font-size:11px">Something on the side</div>
  <div class="extra-card" style="left:14px;width:226px;top:434px"><h4>Crisps selection</h4><small>3 bags of crisps</small><span class="cost">+ $5.00</span><i class="plus"></i></div>
  <div class="extra-card" style="left:254px;width:80px;top:434px"><h4>kegerator</h4><small>Keep your keg</small></div>
  <div class="checkout"><div class="total"><span>Total:</span><span>+ $125.00</span></div><div class="btn">Go to checkout</div></div>
  <div class="home-bar" style="bottom:4px"></div>
</section>

<!-- Some Extra -->
<section class="phone wide" style="left:648px;top:2280px;width:292px">
  <div class="status"><span>9:10</span><span class="right"><svg width="11" height="8"><path d="M0 3Q5.5-1 11 3L5.5 8Z" fill="#2a2418"/></svg>69% <svg width="5" height="8"><rect width="5" height="8" rx="1" fill="#2a2418"/></svg></span></div>
  <svg class="back" style="top:48px" width="18" height="12"><path d="M17 6H2M7 1L2 6L7 11" stroke="#5c4a26" stroke-width="1.6" fill="none"/></svg>
  <h1 class="title" style="top:78px">Some Extra...</h1>
  <div class="extra-row" style="top:124px">
    <div class="thumb" role="img" aria-label="Pint of beer with crisps" style="background:linear-gradient(135deg,#2b2b2b,#d9a23c 55%,#3a3a3a)"></div>
    <h4>Crisps selection</h4><small>3 bags of crisps</small><span class="cost">+ $5.00</span><i class="plus"></i>
  </div>
  <div class="extra-row" style="top:214px">
    <div class="thumb" role="img" aria-label="Plain white branded T-shirts" style="background:linear-gradient(135deg,#e9e9e9,#fafafa 50%,#cfcfcf)"></div>
    <h4>2x T-shirts</h4><small>Branded T-shirts</small><span class="cost">+ $25.00</span><i class="plus"></i>
  </div>
  <div class="checkout"><div class="total"><span>Total:</span><span>+ $125.00</span></div><div class="btn">Continue to checkout</div></div>
  <div class="home-bar" style="bottom:4px"></div>
</section>

</body>
</html>
```